TRELBY Construction Group business card for distribution

A business card detailing our services, with our phone number and email address.
- Groundworks / Foundations / Drainage
- Landscaping / Hard Landscaping / Patios / Decking
- Fencing
The card should include company logo and be in the same colours.

Target Market(s)
Domestic Houses
Industry/Entity Type
Construction
Contact Information for Business Card
Phone Number - 07731 248 905 / 07612093184. Email address: trelbygroup@fenwickmail.com
Font styles to use
Serif
Sans Serif
Colors
F0912C
F2A743
F7CA91
FBE8D2
FDF5EE
Requirements
Must have
- Contact numbers. Photos of past work. Company Logo

Nice to have
- Company Logo

```html
<!DOCTYPE html>
<html lang="en">
<head>
<meta charset="utf-8">
<title>TRELBY Construction Group – Business Card</title>
<link rel="stylesheet" href="https://fonts.googleapis.com/css2?family=Montserrat:wght@500;600;700&display=swap">
<style>
  :root {
    --backdrop: #c9c9c9;
    --card: #ffffff;
    --ink: #231f20;
    --text: #2b2b2b;
    --accent: #f0912c;
    --paper-on-dark: #ffffff;
  }
  * { margin: 0; padding: 0; box-sizing: border-box; }
  html, body {
    width: 1079px; height: 1200px; overflow: hidden;
    background: var(--backdrop);
    font-family: "Montserrat", Arial, sans-serif;
  }
  .sheet {
    width: 1079px; height: 1200px;
    display: flex; flex-direction: column;
    align-items: center; justify-content: center; gap: 58px;
  }
  .card {
    width: 900px; height: 515px; display: block;
    background: var(--card);
    box-shadow: 0 6px 18px rgba(0,0,0,0.12);
  }
  .band-dark { fill: var(--ink); }
  .band-accent { fill: var(--accent); }
  .wordmark-name { font-size: 52px; font-weight: 700; fill: var(--ink); letter-spacing: 1px; }
  .wordmark-sub { font-size: 16.5px; font-weight: 700; fill: var(--ink); letter-spacing: 1.3px; }
  .header-title { font-size: 18px; font-weight: 700; fill: var(--paper-on-dark); letter-spacing: 0.6px; }
  .contact { font-size: 12.5px; font-weight: 500; fill: var(--text); }
  .tag-label { font-size: 14px; font-weight: 700; fill: var(--paper-on-dark); }
  .service { font-size: 12.5px; font-weight: 500; fill: var(--text); }
  .icon { fill: none; stroke: var(--text); stroke-width: 1; }
</style>
</head>
<body>
<main class="sheet">

  <!-- Card front -->
  <svg class="card card-front" viewBox="0 0 517 296" role="group" aria-label="Business card front">
    <rect class="wordmark-mark" x="112" y="112" width="22" height="22" fill="var(--accent)"/>
    <text class="wordmark-name" x="144" y="134">TRELBY</text>
    <text class="wordmark-sub" x="112" y="198">CONSTRUCTION GROUP LTD</text>

    <polygon class="band-accent" points="160,264 355,264 361,274 154,274"/>
    <polygon class="band-dark" points="26,274 491,274 501,287 16,287"/>
  </svg>

  <!-- Card back -->
  <svg class="card card-back" viewBox="0 0 517 296" role="group" aria-label="Business card back">
    <polygon class="band-dark" points="0,24 416,24 398,59 0,59"/>
    <text class="header-title" x="20" y="48">TRELBY CONSTRUCTION GROUP LTD</text>

    <g class="contact-list">
      <circle class="icon" cx="24" cy="94" r="3"/>
      <text class="contact" x="33" y="98">07731 248 905</text>
      <text class="contact" x="33" y="115">07612093184</text>
      <circle class="icon" cx="24" cy="135" r="3"/>
      <text class="contact" x="33" y="139">trelbygroup@fenwickmail.com</text>
    </g>

    <polygon class="band-accent" points="0,164 100,164 92,182 0,182"/>
    <text class="tag-label" x="20" y="178">services</text>

    <g class="service-list">
      <text class="service" x="20" y="207">Groundworks</text>
      <text class="service" x="20" y="230">Patios</text>
      <text class="service" x="136" y="207">Foundations</text>
      <text class="service" x="136" y="230">Decking</text>
      <text class="service" x="243" y="207">Drainage</text>
      <text class="service" x="243" y="230">Fencing</text>
      <text class="service" x="336" y="207">Landscaping</text>
      <text class="service" x="336" y="230">Hard Landscaping</text>
    </g>

    <polygon class="band-accent" points="160,264 355,264 361,274 154,274"/>
    <polygon class="band-dark" points="25,274 491,274 501,287 15,287"/>
  </svg>

</main>
</body>
</html>
```